In-Aisle Customer Special Order Process and FAQ

This infographic/brochure is intended for owners of Birch Tool Depot retail stores who I'm looking to inform about a new process for managing customer special orders. There will be two pages to this infographic / FAQ.

The first page I am looking for a very unique and creative way to educate them on the steps needed to process a customer special order. The two PowerPoint slides I attached is the content for this process. I'm looking to illustrate this information in a very fun and differentiated way that will catch the Birch Tool Depot owners' attention! It must stand out. Right now, the way that it is laid out is boring, unattractive to look at, and too cluttered. I will need all this content, but it will need to be formatted and designed in a much, much better way. Note that step 7 could be either an in-store pick-up or deliver (not both), so the infographic must make that clear.

* Use logos provided. The red vest logo is the mobile app

The second page is a frequently asked question section. This should be in a two column form and match the design of the first page.

Feel free to use some of the images I provided, but not necessary.

Target Market(s)

Birch Tool Depot Store Owners

Font styles to use
Serif

Colors
EB3D1F
EC4F4E
F09395
F8D3D4
FCEDEE

Requirements
Must have
• Birch Tool Depot red and black colors; 8-1/2x11; 2 pages, front and back, Super creative, different looking, eye catching, use all the content I provided. Must include each step, system touchpoints, Lead/location, actions, and outcomes; size 11 font or bigger
Nice to have
• Some of the photos I sent

```html
<!DOCTYPE html>
<html lang="en">
<head>
<meta charset="utf-8">
<title>In-Aisle Customer Special Order Process and FAQs</title>
<link href="https://fonts.googleapis.com/css2?family=Open+Sans:ital,wght@0,400;0,600;0,700;0,800;1,600;1,700;1,800&display=swap" rel="stylesheet">
<style>
:root{
  --red:#e0261b;
  --red-soft:#ec4f4e;
  --pink:#f8d3d4;
  --ink:#111;
  --text:#2b2b2b;
  --muted:#555;
  --paper:#ffffff;
  --stage:#2a2a2a;
}
*{box-sizing:border-box;margin:0;padding:0}
html,body{width:1200px;height:2179px;overflow:hidden;background:var(--stage);font-family:"Open Sans",Arial,sans-serif;color:var(--text)}
.page{position:absolute;left:198px;width:804px;height:1040px;background:var(--paper);overflow:hidden;box-shadow:0 6px 24px rgba(0,0,0,.5)}
.process{top:36px;background:#e9e9e9}
.faq{top:1104px;background:#ececec}

/* header page 1 */
.masthead{position:relative;height:196px;background:var(--ink)}
.hero-photo{position:absolute;right:0;top:0;width:430px;height:196px;background:linear-gradient(100deg,#3a2a26 0%,#8a5a48 35%,#c9372c 70%,#e24a3a 100%)}
.brand{position:absolute;left:24px;top:30px;display:flex;align-items:center;gap:8px;font-weight:700;font-size:13px;color:#fff;text-transform:uppercase;letter-spacing:.4px}
.brand-mark{width:12px;height:12px;background:var(--red)}
.title-band{position:absolute;left:0;height:40px;background:var(--red);color:#fff;font-style:italic;font-weight:800;font-size:26px;padding:2px 24px;white-space:nowrap}
.title-band.one{top:82px;width:330px}
.title-band.two{top:126px;width:380px;left:12px;border-bottom:3px solid #fff}

.steps{display:grid;grid-template-columns:repeat(3,1fr);gap:10px;padding:12px 12px}
.step{background:var(--paper);height:268px;padding:0 0 8px;font-size:7.6px;line-height:1.3;position:relative}
.step-title{display:inline-block;background:var(--red);color:#fff;font-style:italic;font-weight:800;font-size:14px;padding:3px 22px 3px 10px;clip-path:polygon(0 0,100% 0,92% 100%,0 100%)}
.step-title small{font-size:9px;font-weight:700}
.touchpoint{display:flex;align-items:center;gap:6px;padding:6px 10px 0;font-style:italic;color:var(--muted)}
.sys{font-style:normal;font-weight:800;font-size:9px;color:var(--ink)}
.sys.blue{color:#1e5aa8}
.app{display:flex;align-items:center;gap:3px;font-style:normal;font-weight:700;font-size:7px;color:var(--red)}
.app i{display:inline-block;width:9px;height:9px;background:var(--red)}
.lead{padding:6px 10px 0;color:var(--muted);font-style:italic}
.lead b{display:block;color:var(--ink);font-style:italic}
.actions{margin:6px 10px 0;padding:5px 8px;color:#fff}
.actions.red{background:var(--red)}
.actions.dark{background:var(--ink)}
.actions h4,.outcomes h4{font-size:8px;font-weight:800}
ul{padding-left:10px}
.outcomes{padding:6px 10px 0}
.outcomes h4{color:var(--ink)}

/* faq page */
.faq-head{height:78px;background:var(--ink);color:#fff;display:flex;align-items:center;justify-content:center;font-style:italic;font-weight:700;font-size:17px;border-bottom:4px solid var(--red)}
.faq-cols{display:grid;grid-template-columns:1fr 1fr;gap:26px;padding:22px 24px 0}
.qa{margin-bottom:16px}
.q{background:var(--red);color:#fff;font-weight:700;font-size:8.6px;line-height:1.35;padding:7px 14px;clip-path:polygon(0 0,100% 0,97% 100%,0 100%);display:flex;gap:8px}
.q span{flex:0 0 auto}
.a{font-size:8px;line-height:1.5;padding:8px 4px 0;text-align:justify}
.a ul{margin-top:2px}
.faq-foot{position:absolute;left:24px;bottom:30px;display:flex;align-items:center;gap:8px;font-weight:700;font-size:13px;color:var(--ink);text-transform:uppercase;letter-spacing:.4px}
</style>
</head>
<body>

<section class="page process">
  <header class="masthead">
    <div class="hero-photo" role="img" aria-label="Photo of a smiling customer with a store associate in a red vest in the aisle"></div>
    <div class="brand"><span class="brand-mark"></span><span>Birch Tool Depot · Store Systems &amp; Operations</span></div>
    <h1 class="title-band one">In-Aisle Customer</h1>
    <h1 class="title-band two">Special Order Process</h1>
  </header>

  <div class="steps">
    <article class="step">
      <h2 class="step-title">#1 Order Entry</h2>
      <div class="touchpoint">System Touchpoint <span class="sys">BirchNet</span> or <span class="app"><i></i>Birch Mobile</span></div>
      <p class="lead">Lead / Location<b>Sales Associate In-Aisle / Hub</b></p>
      <div class="actions red"><h4>Actions</h4><ul><li>Create Stock Reserve or Customer Priority Order</li><li>Ask about assembly and/or home delivery</li><li>Sell in item's order multiple</li><li>Communicate ETA</li></ul></div>
      <div class="outcomes"><h4>Outcomes</h4><ul><li>Order transmitted to Birch RSC</li><li>Order confirmation sent to customer</li><li>Sends order into Falcon as a Special Order</li><li>Updates BirchNet's Deliveries &amp; Services App</li></ul></div>
    </article>

    <article class="step">
      <h2 class="step-title">#2 Complete POS Trx</h2>
      <div class="touchpoint">System Touchpoint <span class="sys blue">CORVIA</span></div>
      <p class="lead">Lead / Location<b>Cashier at POS / Hub</b></p>
      <div class="actions dark"><h4>Actions</h4><ul><li>Search in Falcon by customer phone #</li><li>Import order into POS</li><li>Take 100% Deposit</li><li>Ring up items being taken today separately</li><li>Provide receipt to customer and thank them</li></ul></div>
      <div class="outcomes"><h4>Outcomes</h4><ul><li>Creates SKU in Falcon, if it hadn't existed</li><li>Committed Qty. updated</li><li>Deposit amount recorded in Falcon</li></ul></div>
    </article>

    <article class="step">
      <h2 class="step-title">#3 Receive</h2>
      <div class="touchpoint">System Touchpoint <span class="app"><i></i>Birch Mobile</span></div>
      <p class="lead">Lead / Location<b>Designated Receivers in Back Room</b></p>
      <div class="actions red"><h4>Actions</h4><ul><li>Pull special orders via Sort and Seg feature</li><li>Scan totes with Special Orders</li><li>Print pick sheets</li></ul></div>
      <div class="outcomes"><h4>Outcomes</h4><ul><li>Prepares product for invoicing and staging</li></ul></div>
    </article>

    <article class="step">
      <h2 class="step-title">#4 Invoice</h2>
      <div class="touchpoint">System Touchpoint <span class="sys blue">CORVIA</span></div>
      <p class="lead">Lead / Location<b>Back Office Store Associate/ Back Office</b></p>
      <div class="actions dark"><h4>Actions</h4><ul><li>Reference order via pick sheets</li><li>Ensure no remaining balance due</li><li>Staple invoice to pick sheet</li></ul></div>
      <div class="outcomes"><h4>Outcomes</h4><ul><li>Qty. On Hand decreased</li><li>Committed Qty. relieved</li><li>Sales transaction recorded</li></ul></div>
    </article>

    <article class="step">
      <h2 class="step-title">#5 Stage</h2>
      <div class="touchpoint">System Touchpoint <span class="app"><i></i>Birch Mobile</span></div>
      <p class="lead">Lead / Location<b>Designated Staff / Staging Area</b></p>
      <div class="actions red"><h4>Actions</h4><ul><li>Review pick sheets and sort them by 1) in-store pickup, no assembly 2) assembly, and 3) delivery, no assembly</li><li>Cross-reference sheets against product</li><li>Receive orders via fulfill customer order feature</li></ul></div>
      <div class="outcomes"><h4>Outcomes</h4><ul><li>If in-store pick up, notification sent to customer</li><li>If to be assembled or delivered, orders are moved to Order Prep feature in mobile app</li></ul></div>
    </article>

    <article class="step">
      <h2 class="step-title">#6 Assemble <small>(when applicable)</small></h2>
      <div class="touchpoint">System Touchpoint <span class="app"><i></i>Birch Mobile</span></div>
      <p class="lead">Lead / Location<b>Designated Staff / Staging Area</b></p>
      <div class="actions dark"><h4>Actions</h4><ul><li>Physically assemble product</li><li>Advance order via Order Prep feature</li></ul></div>
      <div class="outcomes"><h4>Outcomes</h4><ul><li>If order is an in-store pick up, notification sent to customer</li><li>If order is to be delivered, this moves order to Ready for Delivery status in mobile app</li><li>Delivery notification sent to customer on delivery date</li></ul></div>
    </article>

    <article class="step">
      <h2 class="step-title">#7 In-Store Pick-Up</h2>
      <div class="touchpoint">System Touchpoint <span class="app"><i></i>Birch Mobile</span></div>
      <p class="lead">Lead / Location<b>Cashier or Sales Associate In-Aisle / Hub</b></p>
      <div class="actions red"><h4>Actions</h4><ul><li>Customer arrives</li><li>Complete pick up via the Ready for Pickup feature</li><li>Locate order in staging area</li><li>Validate pick sheet, invoice and order paid in full</li><li>Thank customer</li></ul></div>
      <div class="outcomes"><h4>Outcomes</h4><ul><li>Closed order</li><li>Happy customer</li></ul></div>
    </article>

    <article class="step">
      <h2 class="step-title">Deliver
        <svg width="16" height="10" viewBox="0 0 16 10" aria-hidden="true"><rect x="0" y="1" width="10" height="6" fill="#fff"/><path d="M10 3h3l2 2v2h-5z" fill="#fff"/><circle cx="3" cy="8.5" r="1.5" fill="#fff"/><circle cx="12" cy="8.5" r="1.5" fill="#fff"/></svg>
      </h2>
      <div class="touchpoint">System Touchpoint <span class="app"><i></i>Birch Mobile</span></div>
      <p class="lead">Lead / Location<b>Designated Associate / Delivery Destination</b></p>
      <div class="actions dark"><h4>Actions</h4><ul><li>Pack up product/paperwork</li><li>Create route in Needs Delivery feature</li><li>Load up delivery vehicle</li><li>Contact customer to provide time range</li><li>Validate pick sheet, invoice and order paid in full</li><li>Take signature where applicable</li><li>Take photo for unattended deliveries</li><li>Complete delivery in Mobile</li><li>Thank customer</li></ul></div>
      <div class="outcomes"><h4>Outcomes</h4><ul><li>Closed order</li><li>Happy customer</li></ul></div>
    </article>

    <article class="step">
      <h2 class="step-title">Miscellaneous</h2>
      <div class="touchpoint">System Touchpoint <span class="sys blue">CORVIA</span> or <span class="app"><i></i>Birch Mobile</span></div>
      <p class="lead">Lead / Location<b>Back Office Store Associate / Back Office</b></p>
      <div class="actions red"><h4>Actions</h4><ul><li>Location code non-stocked special orders as 'DNRSP'</li><li>Flag large quantities as unusual usage in ITR</li><li>Review open orders from POS or BirchNet Customer Order Tracking</li></ul></div>
      <div class="outcomes"><h4>Outcomes</h4><ul><li>Review the sales performance of special order items</li><li>Keeps items from being reordered</li><li>Addresses order point issues</li><li>Remedies overdue outstanding orders</li></ul></div>
    </article>
  </div>
</section>

<section class="page faq">
  <header class="faq-head">~ In-Aisle Customer Special Orders - FAQs ~</header>
  <div class="faq-cols">
    <div class="col">
      <div class="qa"><p class="q"><span>1.</span>What is meant by "In-Aisle Customer Special Orders" and what kind of impact can they have on my business?</p>
        <p class="a">Special orders are generally characterized by 1) providing the ability to sell items you don't currently stock or 2) reserving an unusually large amount of a regularly stocked product, not being fully filled from the store. Special orders can be a key market differentiator and ultimately add incremental profitability to your bottom line. The average ticket at Birch for a special order is roughly $120!</p></div>
      <div class="qa"><p class="q"><span>2.</span>My current special order process is slow and cumbersome. How has the process become simpler to manage?</p>
        <p class="a">With recent enhancements, you now have the integrated ability to use BirchNet and the Retailer Mobile App to process special orders within Falcon. As a result, the time and the number of steps to process special orders is substantially reduced. Also, to maximize efficiencies, the Birch Retail Mobile Assistant has been updated to improve and manage the receipt, staging, pick up, and delivery processes.</p></div>
      <div class="qa"><p class="q"><span>3.</span>We use the mobile for special orders, but there are times in the process it is more convenient to use a computer terminal. Has there been any changes here?</p>
        <p class="a">One of bigger enhancements rolled out is that BirchNet can now be used for customer special order entry. Specifically, using BirchNet, customer orders can be processed as a stock reserve or customer priority order. Doing so then brings the information into your Falcon system to manage the order in POS, and adds the item into your inventory, if not already on file.</p></div>
      <div class="qa"><p class="q"><span>4.</span>Super important to the special orders is communicating back to the customer the status of their order. How is this accomplished with this experience?</p>
        <p class="a">During the order entry process, the Sales Associate obtains a phone number from the customer as to where to receive notifications. In turn, customers receive notifications when their order is confirmed, when the order is ready for pick up, and the scheduled delivery date.</p></div>
      <div class="qa"><p class="q"><span>5.</span>I hear different things. When is the right time to invoice the special order?</p>
        <p class="a">Under the enhanced special order process, process them immediately after receipt from the RSC. Upon completion, sales are recorded in Falcon, committed quantities decreased, and the status of the order updated in your mobile app.</p></div>
    </div>
    <div class="col">
      <div class="qa"><p class="q"><span>6.</span>I see the value in the process, but I would like more understanding to implement. What do I do?</p>
        <p class="a">Under the enhanced special order process, process them immediately after receipt from the RSC. Upon completion, sales are recorded in Falcon, committed quantities decreased, and the status of the order updated in your mobile app.</p></div>
      <div class="qa"><p class="q"><span>7.</span>From time to time, customers call in asking for updates to their special orders, which we don't have a really good process for checking on efficiently. Has anything changed here?</p>
        <p class="a">Yes. Moving forward, in these instances, leverage BirchNet or the Retailer Mobile App Customer Order Tracking lookup. Doing so allows you to search the status of an order by last name, and order number. Beyond orders taken by the Retailer Mobile App within BirchNet, .com orders are also captured in these programs.</p></div>
      <div class="qa"><p class="q"><span>8.</span>What are some important but underutilized best practices I should be doing with every special order I process in the aisle to help ensure an effective process?</p>
        <div class="a">Though the Birch Way of Retailing In-Aisle Special Orders document outlines each of best practice, some of the top ones include:
          <ul><li>Inform customer of your policy to have orders picked up within five days of it being ready.</li><li>Sell the item in the order multiple in which it comes in, particularly if you don't stock the product.</li><li>For a clean process, do not include any items to be taken by the customer that day under the same transaction as the special order. Ring those up separately.</li></ul></div></div>
      <div class="qa"><p class="q"><span>9.</span>I reviewed the BWOR best practice. Why do I need to take 100% deposit?</p>
        <p class="a">Studies show that 8% of customer special orders that get are started never get picked up, resulting in a potential and sizable profit loss. Taking a full deposit eliminates the financial risk on the part of the store, and facilitates a sense of urgency for the customer to pick the product up.</p></div>
      <div class="qa"><p class="q"><span>10.</span>Who do I contact with any further questions and support?</p>
        <p class="a">For further details about the customer special orders, contact the Store Systems and Operations team.<br>P: +1 630.555.0147<br>E: storesystems@birchtooldepot.com</p></div>
    </div>
  </div>
  <footer class="faq-foot"><span class="brand-mark"></span><span>Birch Tool Depot · Store Systems &amp; Operations</span></footer>
</section>

</body>
</html>
```